New business card design

I need original, modern, business looking but dzen (minimalistic) looking design.
Also refer to websit qvtrenda.ru

Text is

Зорин Виктор, PMP
Партнер

Моб. +7 (915) 460 1897
info@qvtrenda.ru
Москва, Россия, 117358, ул. Берёзовая 27/2
=====================

Zorin Viktor, PMP
Partner

Mob. +7 (915) 460 1897
info@qvtrenda.ru
Moscow, Russia,117358, Beryozovaya 27/2

```html
<!DOCTYPE html>
<html lang="ru">
<head>
<meta charset="utf-8">
<title>QVTrenda — визитная карточка</title>
<link rel="stylesheet" href="https://fonts.googleapis.com/css2?family=PT+Serif:wght@400&display=swap">
<style>
  :root {
    --backdrop: #e4e6e8;
    --card: #ffffff;
    --ink: #1c1c1c;
    --cyan: #29c0dc;
    --sky: #6fcdf2;
    --blue: #1a7fc4;
    --deep-blue: #0f6fb4;
    --shadow: rgba(0, 0, 0, 0.14);
  }
  * { box-sizing: border-box; margin: 0; padding: 0; }
  html, body {
    width: 1200px;
    height: 926px;
    overflow: hidden;
    background: var(--backdrop);
    font-family: "PT Serif", "Times New Roman", serif;
    color: var(--ink);
  }
  .sheet {
    width: 1200px;
    height: 926px;
    display: flex;
    flex-direction: column;
    align-items: center;
    justify-content: center;
    gap: 40px;
  }
  .card {
    position: relative;
    width: 720px;
    height: 400px;
    background: var(--card);
    box-shadow: 0 6px 22px var(--shadow);
    overflow: hidden;
  }

  /* Back: brand side */
  .card--brand {
    display: flex;
    align-items: center;
    justify-content: center;
  }
  .brand {
    display: flex;
    align-items: center;
    gap: 22px;
  }
  .brand__mark {
    width: 78px;
    height: 78px;
    background: var(--sky);
  }
  .brand__name {
    font-size: 74px;
    color: var(--ink);
    letter-spacing: 0.5px;
  }

  /* Front: contact side */
  .card--contact .brand {
    position: absolute;
    top: 34px;
    left: 44px;
    gap: 12px;
  }
  .card--contact .brand__mark { width: 30px; height: 30px; }
  .card--contact .brand__name { font-size: 30px; }

  .person {
    position: absolute;
    top: 130px;
    left: 44px;
  }
  .person__name {
    font-size: 24px;
    font-weight: 400;
  }
  .person__cert {
    font-size: 17px;
    color: var(--blue);
  }
  .person__role {
    font-size: 17px;
    color: var(--blue);
    margin-top: 2px;
  }

  .contacts {
    position: absolute;
    top: 212px;
    left: 44px;
    list-style: none;
  }
  .contacts__item {
    display: flex;
    align-items: center;
    gap: 12px;
    height: 28px;
    font-size: 17px;
  }
  .contacts__icon {
    width: 24px;
    height: 24px;
    background: var(--blue);
    display: flex;
    align-items: center;
    justify-content: center;
  }
  .contacts__icon svg { width: 15px; height: 15px; }

  .band {
    position: absolute;
    left: 0;
    right: 0;
    bottom: 0;
    height: 62px;
    background: var(--cyan);
  }
  .decor {
    position: absolute;
    right: 0;
    bottom: 0;
    width: 270px;
    height: 270px;
    background: linear-gradient(150deg, var(--deep-blue) 0%, var(--sky) 55%, var(--cyan) 100%);
  }
</style>
</head>
<body>
<main class="sheet">

  <section class="card card--brand">
    <div class="brand">
      <span class="brand__mark"></span>
      <span class="brand__name">QVTrenda</span>
    </div>
  </section>

  <section class="card card--contact">
    <div class="band"></div>
    <div class="decor" role="img" aria-label="Декоративная композиция в голубых и синих тонах"></div>

    <div class="brand">
      <span class="brand__mark"></span>
      <span class="brand__name">QVTrenda</span>
    </div>

    <div class="person">
      <h1 class="person__name">Зорин Виктор,<span class="person__cert">PMP</span></h1>
      <p class="person__role">Партнер</p>
    </div>

    <ul class="contacts">
      <li class="contacts__item">
        <span class="contacts__icon">
          <svg viewBox="0 0 16 16" fill="none" stroke="#fff" stroke-width="1.6"><rect x="4.5" y="1.5" width="7" height="13" rx="1.2"/><line x1="7" y1="12" x2="9" y2="12"/></svg>
        </span>
        +7 (915) 460 1897
      </li>
      <li class="contacts__item">
        <span class="contacts__icon">
          <svg viewBox="0 0 16 16" fill="none" stroke="#fff" stroke-width="1.5"><rect x="1.5" y="3.5" width="13" height="9"/><polyline points="1.5,3.5 8,9 14.5,3.5"/></svg>
        </span>
        info@qvtrenda.ru
      </li>
      <li class="contacts__item">
        <span class="contacts__icon">
          <svg viewBox="0 0 16 16" fill="#fff"><polygon points="8,1.5 15,8 13,8 13,14.5 10,14.5 10,10 6,10 6,14.5 3,14.5 3,8 1,8"/></svg>
        </span>
        Москва, Россия, 117358, ул. Берёзовая 27/2
      </li>
    </ul>
  </section>

</main>
</body>
</html>
```